Advertising poster for podcast event

"The Lantern Table" is one of the most popular podcasts in Switzerland (https://listen.harbofeed.example/show/4kqpVXRT219LmNaw8BYdE5). It is hosted by the two radio DJs Lukas Brenner and Rafael Tanner. For a series of live shows where the podcast is recorded with an audience, we need a design of a poster. This should have the format A3 high. In addition, the image must be used that was uploaded here, because this is the cover photo with which you can always recognize the podcast. But what is designed around it is up to you. In addition, it must contain the following text:

- Title of the event:
The lantern table - Live
- Show dates:
Saturday, November 11, 2023 - Solothurn
Wednesday, December 27, 2023 - Berne
Thursday, December 28, 2023 - Berne
- A line with additional information about the presale:
The Dome, information and tickets: www.kuppelfest.example

Target Market(s)

Switzerland

Industry/Entity Type

Entertainment

Requirements
Must have
• The attached image and text according to the briefing.

```html
<!DOCTYPE html>
<html lang="en">
<head>
<meta charset="utf-8">
<title>The Lantern Table – Live Poster</title>
<link href="https://fonts.googleapis.com/css2?family=Oswald:wght@500;600&family=Anton&family=Montserrat:ital,wght@1,800&display=swap" rel="stylesheet">
<style>
  :root{
    --surround:#cbcbcb;
    --night:#0d0838;
    --indigo:#2a2380;
    --violet:#3b2f96;
    --sky:#55c5e8;
    --white:#ffffff;
    --ink:#050314;
  }
  html,body{margin:0;padding:0;overflow:hidden;}
  body{width:904px;height:1200px;background:var(--surround);position:relative;}
  .poster{
    position:absolute;left:88px;top:89px;width:720px;height:1022px;overflow:hidden;
    background:
      radial-gradient(ellipse 70% 45% at 50% 55%, var(--violet) 0%, transparent 70%),
      linear-gradient(180deg, var(--night) 0%, var(--indigo) 35%, #1c1668 70%, var(--ink) 100%);
  }
  .beams{position:absolute;inset:0;}
  .hosts{
    position:absolute;top:0;left:0;right:0;text-align:center;
    font-family:"Oswald",sans-serif;font-weight:600;text-transform:uppercase;line-height:1;
  }
  .hosts .host-one{position:absolute;top:40px;left:0;right:0;font-size:56px;color:var(--white);letter-spacing:-0.5px;}
  .hosts .host-two{position:absolute;top:99px;left:0;right:0;font-size:56px;color:var(--sky);letter-spacing:-0.5px;}
  .cover-art{
    position:absolute;left:80px;top:166px;width:562px;height:355px;
    background:linear-gradient(135deg,#2b2628 0%,#6b4a3a 40%,#d9a58a 60%,#a9bde0 100%);
    border-radius:40px 40px 0 0;opacity:.9;
  }
  .title-frame{position:absolute;left:75px;top:491px;width:577px;height:234px;}
  .title{
    position:absolute;left:75px;top:507px;width:577px;text-align:center;
    font-family:"Anton",sans-serif;text-transform:uppercase;line-height:1;
  }
  .title .line-white{display:block;font-size:80px;color:var(--white);text-shadow:2px 3px 4px rgba(0,0,0,.5);margin-top:20px;}
  .title .line-blue{display:block;font-size:80px;color:var(--sky);text-shadow:2px 3px 4px rgba(0,0,0,.5);}
  .live-tab{
    position:absolute;left:271px;top:703px;width:186px;height:38px;border-radius:19px;
    background:linear-gradient(90deg,var(--ink),#1d1760 50%,var(--ink));
    font-family:"Montserrat",sans-serif;font-style:italic;font-weight:800;
    color:var(--white);font-size:28px;line-height:38px;text-align:center;letter-spacing:1px;
  }
  .dates{position:absolute;top:794px;left:82px;}
  .date-pill{
    position:absolute;top:0;width:175px;height:101px;border:2px solid var(--sky);border-radius:52px;
    background:radial-gradient(ellipse at 50% 40%, #231c78 0%, var(--night) 90%);
    font-family:"Oswald",sans-serif;font-weight:500;text-transform:uppercase;text-align:center;
    font-size:19px;line-height:27px;padding-top:11px;box-sizing:border-box;color:var(--white);
    white-space:nowrap;
  }
  .date-pill .date{color:var(--sky);}
  .footer{position:absolute;left:0;right:0;top:943px;text-align:center;}
  .bar{
    display:inline-flex;align-items:center;height:34px;border:2px solid var(--white);
    border-radius:18px;background:var(--ink);box-sizing:border-box;
    font-family:"Oswald",sans-serif;font-weight:500;text-transform:uppercase;font-size:16px;
    color:var(--white);white-space:nowrap;
  }
  .bar .info{padding:0 10px 0 11px;}
  .bar .url{
    height:34px;margin:-2px -2px -2px 0;padding:0 11px;border-radius:18px;
    background:var(--sky);border:2px solid var(--white);box-sizing:border-box;line-height:30px;
  }
</style>
</head>
<body>
<div class="poster">
  <svg class="beams" width="720" height="1022" viewBox="0 0 720 1022" aria-hidden="true">
    <polygon points="0,0 300,0 0,260" fill="#ffffff" opacity=".04"/>
    <polygon points="0,620 260,560 0,880" fill="#6a5fd0" opacity=".12"/>
    <polygon points="400,820 600,1022 300,1022" fill="#8a7fe6" opacity=".1"/>
    <line x1="0" y1="1000" x2="330" y2="700" stroke="#8a7fe6" stroke-opacity=".3"/>
    <line x1="720" y1="950" x2="520" y2="1022" stroke="#8a7fe6" stroke-opacity=".3"/>
  </svg>

  <div class="hosts">
    <div class="host-one">DJ Lukas Brenner</div>
    <div class="host-two">&amp;&nbsp; DJ Rafael Tanner</div>
  </div>

  <div class="cover-art" role="img" aria-label="Podcast cover artwork of the two hosts"></div>

  <svg class="title-frame" viewBox="0 0 577 234" aria-hidden="true">
    <defs>
      <linearGradient id="rim" x1="0" y1="0" x2="1" y2="1">
        <stop offset="0" stop-color="#ffffff"/>
        <stop offset=".5" stop-color="#8d8fa0"/>
        <stop offset="1" stop-color="#f2f3f7"/>
      </linearGradient>
      <radialGradient id="fill" cx=".5" cy=".3" r=".7">
        <stop offset="0" stop-color="#2a2490"/>
        <stop offset="1" stop-color="#0c0735"/>
      </radialGradient>
    </defs>
    <rect x="4" y="4" width="569" height="226" rx="113" fill="url(#fill)" stroke="url(#rim)" stroke-width="7"/>
    <rect x="14" y="14" width="549" height="206" rx="103" fill="none" stroke="#ffffff" stroke-opacity=".35" stroke-width="1.5"/>
  </svg>

  <div class="title">
    <span class="line-white">The Lantern</span>
    <span class="line-blue">Table</span>
  </div>

  <div class="live-tab">LIVE</div>

  <div class="dates">
    <div class="date-pill" style="left:0">Saturday<br><span class="date">November 11, 2023</span><br>Solothurn</div>
    <div class="date-pill" style="left:193px">Wednesday<br><span class="date">December 27, 2023</span><br>Berne</div>
    <div class="date-pill" style="left:387px">Thursday<br><span class="date">December 28, 2023</span><br>Berne</div>
  </div>

  <div class="footer">
    <div class="bar"><span class="info">The Dome, information and tickets:</span><span class="url">www.kuppelfest.example</span></div>
  </div>
</div>
</body>
</html>
```